New website for Pollard Law Firm at www.keepwinning-example.com

We are a professional law firm located in the Nashville, Tennessee USA area. We focus on personal injury law. We are looking for a slick new website that is user friendly for updating with new blogs, videos, etc. The primary colors should be red, black, and white. It should load extremely fast and have a good mobile component. The pages for the design will include a home page, about us, news, contact us, and practice page. The practice page will be copied for all the practice areas including motor vehicle accidents, slip and fall accidents, dog bites, etc. We have included an image which we would like to include in the new site which shows the color scheme The image is called banner-Car Wreck. The new website should NOT have gavels, court houses, law books, scales or the typical images for a law firm.

Target Market(s)

People in Tennessee involved in accidents

Industry/Entity Type

Legal services, law firm

Coding

Coded - Design and coding required

Number of Pages Required

5+ page

Font styles to use
Serif

Colors
EB3D1F
EC4F4E
F09395
F8D3D4
FCEDEE

Requirements
Should not have
• Gavels, columns, scales, law related images

```html
<!DOCTYPE html>
<html lang="en">
<head>
<meta charset="utf-8">
<title>Pollard Law Firm</title>
<link href="https://fonts.googleapis.com/css2?family=Cinzel:wght@400;600&family=Open+Sans:wght@400;600;700&display=swap" rel="stylesheet">
<style>
:root{
  --red:#EB3D1F;--red2:#EC4F4E;--pink:#F09395;--blush:#F8D3D4;--paper:#FCEDEE;
  --ink:#222;--text:#666;--dark:#1f1f1f;--line:#e6e6e6;--white:#fff;--gold:#f5c518;
}
*{box-sizing:border-box;margin:0;padding:0}
html,body{width:1200px;height:4800px;overflow:hidden}
body{font-family:"Open Sans",Arial,sans-serif;color:var(--text);background:var(--white);font-size:13px;line-height:1.75}
.wrap{width:876px;margin:0 auto;position:relative}
.btn{display:inline-block;border:2px solid var(--red);outline:2px solid var(--red);outline-offset:2px;background:var(--red);color:#fff;font-size:12px;font-weight:600;letter-spacing:1px;text-transform:uppercase;padding:8px 22px;line-height:1.4}
.kicker{color:var(--red);font-size:13px;letter-spacing:5px;text-transform:uppercase;line-height:1.4}
.title{font-family:"Cinzel",Georgia,serif;color:var(--ink);font-weight:600;font-size:36px;line-height:1.15}
.photo{display:block}
.soc{display:inline-block;width:26px;height:26px;border:1px solid #ccc;background:#fff;vertical-align:middle}
.soc.red{background:var(--red);border-color:var(--red)}

/* wordmark */
.wordmark{display:flex;align-items:center;gap:10px;font-family:"Open Sans",Arial,sans-serif;font-weight:700;font-size:24px;line-height:1;color:var(--red);white-space:nowrap}
.wordmark .mark{width:14px;height:14px;background:currentColor;flex:none}
.wordmark.light{color:#fff}

/* header */
.site-header{height:97px}
.site-header .wrap{height:97px}
.site-header .wordmark{position:absolute;left:0;top:34px}
.topbar{position:absolute;right:0;top:16px;display:flex;gap:8px;align-items:center}
.phone-btn{background:var(--red);color:#fff;font-size:13px;padding:4px 16px;display:flex;gap:10px;align-items:center;margin-left:30px;height:34px}
.nav{position:absolute;right:0;top:62px;display:flex;gap:56px;font-size:13px;color:#777}
.nav .on{color:var(--red)}

/* hero */
.hero{height:563px;background:#050505;position:relative;overflow:hidden}
.hero-photo{position:absolute;right:0;top:0;width:760px;height:563px;background:radial-gradient(ellipse at 62% 50%,#c4281c 0%,#7a1410 35%,#2a0a08 65%,#050505 85%)}
.hero-copy{position:absolute;left:162px;top:140px}
.hero-copy .kicker{font-size:14px;letter-spacing:1px}
.hero h1{font-family:"Cinzel",Georgia,serif;color:#fff;font-weight:600;font-size:46px;line-height:1.33;margin:14px 0 30px}

/* about */
.about{height:640px;padding-top:75px}
.about .wrap{display:flex;gap:38px}
.about-media{position:relative;width:378px;height:454px;flex:none}
.about-media .photo{width:378px;height:454px;background:linear-gradient(160deg,#bfc7c9,#7d8a8c 50%,#8b2a2a)}
.play{position:absolute;left:-42px;bottom:-34px}
.about-copy .kicker{margin-bottom:8px}
.about-copy h3{font-size:12px;color:var(--ink);font-weight:700;margin:18px 0 14px}
.about-copy p{font-size:12.5px;line-height:1.72;margin-bottom:16px}
.about-cta{display:flex;align-items:center;gap:28px;margin-top:8px}
.call{display:flex;gap:14px;align-items:center}
.call small{display:block;font-size:11px;color:var(--ink);font-weight:600;line-height:1.2}
.call b{color:var(--red);font-size:15px}

/* practice */
.practice{height:1257px;background:var(--paper);padding-top:84px;text-align:center}
.practice .title{margin:10px 0 40px}
.grid{display:grid;grid-template-columns:438px 438px;grid-auto-rows:337px;text-align:left}
.area{background:#fff;padding:32px 30px}
.area h3{font-family:"Cinzel",Georgia,serif;color:var(--ink);font-size:24px;font-weight:600;line-height:1.2}
.area h4{font-size:11.5px;color:#444;font-weight:600;text-transform:uppercase;margin:10px 0 12px;line-height:1.9}
.area p{font-size:12.5px;margin-bottom:18px}
.area-photo.a1{background:linear-gradient(135deg,#6f8aa4,#c43a26 55%,#41505c)}
.area-photo.a2{background:linear-gradient(135deg,#5b3b24,#8c6a4a 55%,#3a2a1e)}
.area-photo.a3{background:linear-gradient(135deg,#d7dde2,#8a9aa6 55%,#7a2f2a)}

/* testimonials */
.testimonials{height:507px;position:relative;text-align:center;padding-top:82px;color:#fff;background:linear-gradient(90deg,#e0473f,#ef5a47 50%,#e0473f)}
.testimonials .kicker{color:#fff}
.testimonials .title{color:#fff;margin:6px 0 44px}
.quote-box{position:relative;width:799px;height:210px;margin:0 auto;border:2px solid rgba(255,255,255,.45);padding:52px 60px 0;font-size:14px;line-height:1.9}
.avatar{position:absolute;left:50%;top:-34px;margin-left:-34px;width:68px;height:68px;border-radius:50%;background:var(--gold);border:4px solid #f7d8a0;color:#fff;font-size:26px;line-height:60px;font-family:"Cinzel",Georgia,serif}
.qmark{position:absolute;font-family:Georgia,serif;font-size:56px;color:var(--gold);line-height:1}
.stars{color:var(--gold);letter-spacing:3px;margin-top:6px;line-height:1.4}
.author{font-family:"Cinzel",Georgia,serif;font-size:16px;line-height:1.4}
.arrows{position:absolute;left:50%;bottom:-22px;margin-left:-48px;display:flex;gap:4px}
.arrows span{width:44px;height:44px;border:2px solid rgba(255,255,255,.5);color:var(--gold);font-size:20px;line-height:38px;background:var(--red2)}

/* news */
.news{height:708px;padding-top:82px;text-align:center}
.news .title{margin:6px 0 28px}
.news-grid{display:flex;gap:16px;text-align:left}
.feature{width:432px;height:449px;border:1px solid var(--line);position:relative}
.feature .photo{height:257px;background:linear-gradient(180deg,#8fa3b5,#d98a4c 55%,#3a3a3a)}
.tag{position:absolute;left:10px;top:12px;background:#fff;color:var(--red);border:1px solid var(--red);font-size:9px;padding:0 6px;text-transform:uppercase}
.date{position:absolute;right:0;top:227px;background:var(--red);color:#fff;text-align:center;width:46px;padding:4px 0;line-height:1.1;font-size:10px}
.date b{display:block;font-size:20px}
.feature .body{padding:18px 20px}
.feature h3,.item h3{font-family:"Cinzel",Georgia,serif;color:var(--ink);font-weight:600}
.feature h3{font-size:17px;line-height:1.35;margin-bottom:10px}
.feature p{font-size:12.5px}
.more{color:var(--red);font-size:12px;font-weight:600;letter-spacing:1px}
.list{flex:1;display:flex;flex-direction:column;gap:16px}
.item{display:flex;border:1px solid var(--line);height:101px;overflow:hidden}
.item .photo{width:150px;flex:none}
.item .txt{padding:8px 14px;font-size:11px;line-height:1.5}
.meta{color:var(--red);font-size:9.5px;text-transform:uppercase}
.item h3{font-size:13.5px;line-height:1.25;margin:3px 0}
.item i{font-style:normal;color:var(--red)}
.n1{background:linear-gradient(135deg,#4a5b70,#c7b8a8)}.n2{background:linear-gradient(135deg,#2b3440,#9aa7b3)}
.n3{background:linear-gradient(135deg,#d66a3a,#6f7f4a)}.n4{background:linear-gradient(135deg,#5a6e82,#e3ded6)}
.view{text-align:center;margin-top:34px}

/* consultation */
.consult{height:712px;background:#fff;padding-top:65px}
.consult-frame{width:915px;margin:0 auto;border:10px solid var(--red2);display:flex;height:559px}
.form{width:454px;padding:26px 24px 0 36px}
.form h2{font-family:"Cinzel",Georgia,serif;color:var(--ink);font-weight:400;font-size:22px;line-height:1.3;margin-bottom:14px;white-space:nowrap}
.field{margin-bottom:12px}
.field label{display:block;font-size:12.5px;color:#555;line-height:1.6}
.field .box{border:1px solid #ddd;height:28px;font-size:11px;padding:5px 12px;color:#666;line-height:1.5;display:flex;justify-content:space-between}
.field .box.tall{height:46px}
.submit{background:var(--red);color:#fff;text-align:center;font-family:"Cinzel",Georgia,serif;font-size:14px;padding:7px;margin-top:20px;line-height:1.5}
.consult-photo{flex:1;background:linear-gradient(135deg,#f2efe9,#c9b6a3 55%,#8a7766)}

/* footer */
.site-footer{height:315px;background:var(--dark);color:#ddd;padding-top:40px}
.foot-top{display:flex;justify-content:space-between;align-items:flex-start;height:85px;border-bottom:1px solid #3a3a3a}
.foot-nav{display:flex;gap:56px;font-size:13px;color:#ddd;margin-top:2px}
.foot-nav .on{color:var(--red)}
.contacts{display:flex;justify-content:space-between;align-items:center;border-bottom:1px solid #3a3a3a;height:123px}
.contact{display:flex;gap:14px;align-items:center;font-size:12.5px;line-height:1.5}
.contact b{display:block;font-weight:600}
.contact + .contact{border-left:1px solid #3a3a3a;padding-left:44px}
.copy{display:flex;justify-content:space-between;align-items:center;font-size:11.5px;padding-top:18px}
.copy .soc{border-color:#888;background:transparent;margin-left:8px}
.copy .soc.red{background:var(--red);border-color:var(--red)}
</style>
</head>
<body>

<header class="site-header">
  <div class="wrap">
    <div class="wordmark"><span class="mark"></span>Pollard Law Firm</div>
    <div class="topbar">
      <span class="soc" aria-label="Social link"></span>
      <span class="soc red" aria-label="Social link"></span>
      <span class="soc" aria-label="Social link"></span>
      <span class="soc" aria-label="Social link"></span>
      <span class="phone-btn">
        <svg width="16" height="16" viewBox="0 0 24 24"><path fill="#fff" d="M6.6 10.8a15 15 0 0 0 6.6 6.6l2.2-2.2a1 1 0 0 1 1-.25 11.4 11.4 0 0 0 3.6.6 1 1 0 0 1 1 1V20a1 1 0 0 1-1 1A17 17 0 0 1 3 4a1 1 0 0 1 1-1h3.5a1 1 0 0 1 1 1c0 1.25.2 2.45.6 3.6a1 1 0 0 1-.25 1z"/></svg>
        (615) 555-0142
      </span>
    </div>
    <nav class="nav"><span class="on">Home</span><span>About Us</span><span>Practice</span><span>News</span><span>Contact Us</span></nav>
  </div>
</header>

<section class="hero">
  <div class="hero-photo" role="img" aria-label="Photo of a red car with a shattered windscreen after a crash"></div>
  <div class="hero-copy">
    <div class="kicker">Pollard Law Firm PLLC</div>
    <h1>DON’T LOSE<br>WHAT’S LEGALLY<br>YOURS</h1>
    <span class="btn">Contact Us</span>
  </div>
</section>

<section class="about">
  <div class="wrap">
    <div class="about-media">
      <div class="photo" role="img" aria-label="Photo of a distressed woman standing beside a crashed car"></div>
      <svg class="play" width="104" height="104" viewBox="0 0 104 104" aria-label="Play video">
        <circle cx="52" cy="52" r="50" fill="#F8D3D4"/><circle cx="52" cy="52" r="42" fill="#EB3D1F"/>
        <path d="M43 34 L70 52 L43 70 Z" fill="#fff"/>
      </svg>
    </div>
    <div class="about-copy">
      <div class="kicker">About Us</div>
      <h2 class="title">Keepwinning Personal<br>Injury Law</h2>
      <h3>WE ARE TRIAL LAWYERS AND WE ARE PROUD OF IT!</h3>
      <p>There are many law firms in Tennessee who claim to be trial lawyers, but their attorneys have never seen a courtroom. We have tried hundreds of cases to verdict and we have helped thousands of people in the Tennessee courts. We fight against billion dollar insurance companies, billion dollar corporations, and the State of Tennessee.. and we win!</p>
      <p>It is very hard not to take each case personally. Our clients include victims of personal injury who did not ask for the pain from a car wreck; professionals who are trying to provide for their family and save their license; and parents falsely accused in a child custody proceeding.</p>
      <div class="about-cta">
        <span class="btn">Read More</span>
        <div class="call">
          <svg width="42" height="42" viewBox="0 0 42 42"><circle cx="21" cy="21" r="20" fill="#fff" stroke="#F8D3D4" stroke-width="2"/><path transform="translate(12 12) scale(.75)" fill="#EB3D1F" d="M6.6 10.8a15 15 0 0 0 6.6 6.6l2.2-2.2a1 1 0 0 1 1-.25 11.4 11.4 0 0 0 3.6.6 1 1 0 0 1 1 1V20a1 1 0 0 1-1 1A17 17 0 0 1 3 4a1 1 0 0 1 1-1h3.5a1 1 0 0 1 1 1c0 1.25.2 2.45.6 3.6a1 1 0 0 1-.25 1z"/></svg>
          <div><small>CALL US</small><b>(615) 555-0142</b></div>
        </div>
      </div>
    </div>
  </div>
</section>

<section class="practice">
  <div class="wrap">
    <div class="kicker">Practice</div>
    <h2 class="title">Areas of Practice</h2>
    <div class="grid">
      <article class="area">
        <h3>Personal Injury</h3>
        <h4>Don’t lose the money which the insurance company is trying to keep from you</h4>
        <p>Our personal injury clients don’t ask to be involved in these types of cases. They don’t ask to be hit by a car, rear ended by a semi, or become the victim of a negligent doctor, and they certainly don’t ask for the pain that follows. Our clients are normal every day people...</p>
        <span class="btn">Read More</span>
      </article>
      <div class="area-photo a1" role="img" aria-label="Photo of a paramedic helping an injured driver beside a damaged car"></div>
      <div class="area-photo a2" role="img" aria-label="Photo of a team of professionals gathered around an office desk"></div>
      <article class="area">
        <h3>Professional Licenses</h3>
        <h4>Don’t lose your license which the state is trying to take away from you</h4>
        <p>Tennessee has thousands of licensed professionals who work hard to provide for their families and who strive for perfection. Just like anyone, many of these professionals take on too much and make mistakes. Whether it is the Tennessee Department of Health or the Department...</p>
        <span class="btn">Read More</span>
      </article>
      <article class="area">
        <h3>Child Custody</h3>
        <h4>Don’t lose your family who you would give anything to keep</h4>
        <p>Children are the most important part of a person’s life. No one can really understand what it means when someone says “I would take a bullet for them,” until they become a parent. In Tennessee, the juvenile courts are designed to protect children from abuse or neglect...</p>
        <span class="btn">Read More</span>
      </article>
      <div class="area-photo a3" role="img" aria-label="Photo of a family meeting with a counsellor in an office"></div>
    </div>
  </div>
</section>

<section class="testimonials" role="region" aria-label="Client testimonials over a faint photo of smiling clients">
  <div class="kicker">Testimonials</div>
  <h2 class="title">What Our Clients Say</h2>
  <div class="quote-box">
    <div class="avatar">J</div>
    <span class="qmark" style="left:26px;top:14px">“</span>
    <span class="qmark" style="right:26px;bottom:-4px">”</span>
    <p>Speak up for those who cannot speak for themselves, for the rights of all who are destitute.<br>Speak up and judge fairly; defend the rights of the poor and needy.”</p>
    <div class="stars">★★★★★</div>
    <div class="author">John Doe</div>
    <div class="arrows"><span>←</span><span>→</span></div>
  </div>
</section>

<section class="news">
  <div class="wrap">
    <div class="kicker">News</div>
    <h2 class="title">Latest News &amp; Updates</h2>
    <div class="news-grid">
      <article class="feature">
        <div class="photo" role="img" aria-label="Photo of a red semi-truck on a highway at sunset"></div>
        <span class="tag">Personal Injury</span>
        <div class="date"><b>01</b>Jul 19</div>
        <div class="body">
          <h3>Trucking Company Offers 6<br>Figure Settlement</h3>
          <p>On a Thursday afternoon, our client was traveling to work when suddenly a semi-truck ran through a stop sign and crashed into the side of our client’s truck causing him...</p>
          <span class="more">READ MORE →</span>
        </div>
      </article>
      <div class="list">
        <div class="item"><div class="photo n1" role="img" aria-label="Photo of a family meeting"></div><div class="txt"><div class="meta">March 14, 2019 • Child Custody</div><h3>DCS Chooses to Dismiss Case</h3>In a case in Nashville, Davidson County, the Tennessee Department of Children’s <i>[+]</i></div></div>
        <div class="item"><div class="photo n2" role="img" aria-label="Photo of an injured driver"></div><div class="txt"><div class="meta">October 1, 2018 • Law, Personal Injury</div><h3>Pollard Obtains Jury Verdict of 61 x Medical Bills</h3>In 2016, a client was traveling down... <i>[+]</i></div></div>
        <div class="item"><div class="photo n3" role="img" aria-label="Photo of paramedics at a crash scene"></div><div class="txt"><div class="meta">August 1, 2018 • Personal Injury</div><h3>Insurance Company Pays for Facial Fractures</h3>On a dark night in Murfreesboro... <i>[+]</i></div></div>
        <div class="item"><div class="photo n4" role="img" aria-label="Photo of a consultation at a desk"></div><div class="txt"><div class="meta">March 14, 2017 • Child Custody</div><h3>Lorem Ipsum is Simply Dummy</h3>Ut enim ad minim veniam, quis nostrud exercitation ullamco laboris nisi ut... <i>[+]</i></div></div>
      </div>
    </div>
    <div class="view"><span class="btn">View All</span></div>
  </div>
</section>

<section class="consult">
  <div class="consult-frame">
    <form class="form">
      <h2>Request a Free Consultation</h2>
      <div class="field"><label>Name*</label><div class="box">Full Name</div></div>
      <div class="field"><label>Email*</label><div class="box">example@gmail.com</div></div>
      <div class="field"><label>Phone</label><div class="box">615</div></div>
      <div class="field"><label>Location</label><div class="box">Where do yo live</div></div>
      <div class="field"><label>Which Type of</label><div class="box">Please Select<span>⌄</span></div></div>
      <div class="field"><label>Description</label><div class="box tall">What happened</div></div>
      <div class="submit">Request a Free Consultation</div>
    </form>
    <div class="consult-photo" role="img" aria-label="Photo of a person using a laptop showing the firm website"></div>
  </div>
</section>

<footer class="site-footer">
  <div class="wrap">
    <div class="foot-top">
      <div class="wordmark light"><span class="mark"></span>Pollard Law Firm</div>
      <nav class="foot-nav"><span class="on">Home</span><span>About Us</span><span>Practice</span><span>News</span><span>Contact Us</span></nav>
    </div>
    <div class="contacts">
      <div class="contact">
        <svg width="42" height="42" viewBox="0 0 42 42"><circle cx="21" cy="21" r="20" fill="#EB3D1F"/><path transform="translate(12 12) scale(.75)" fill="#fff" d="M6.6 10.8a15 15 0 0 0 6.6 6.6l2.2-2.2a1 1 0 0 1 1-.25 11.4 11.4 0 0 0 3.6.6 1 1 0 0 1 1 1V20a1 1 0 0 1-1 1A17 17 0 0 1 3 4a1 1 0 0 1 1-1h3.5a1 1 0 0 1 1 1c0 1.25.2 2.45.6 3.6a1 1 0 0 1-.25 1z"/></svg>
        <div><b>Call Us:</b>(615) 555-0187</div>
      </div>
      <div class="contact">
        <svg width="42" height="42" viewBox="0 0 42 42"><circle cx="21" cy="21" r="20" fill="#EB3D1F"/><rect x="12" y="14" width="18" height="13" fill="#fff"/><path d="M12 14 L21 22 L30 14" fill="none" stroke="#EB3D1F" stroke-width="2"/></svg>
        <div><b>Email Us:</b>office@pollardlawfirm-example.com</div>
      </div>
      <div class="contact">
        <svg width="42" height="42" viewBox="0 0 42 42"><circle cx="21" cy="21" r="20" fill="#EB3D1F"/><path d="M21 11a7 7 0 0 0-7 7c0 5 7 13 7 13s7-8 7-13a7 7 0 0 0-7-7z" fill="#fff"/><circle cx="21" cy="18" r="2.6" fill="#EB3D1F"/></svg>
        <div><b>Address:</b>1200 Maple Ridge Drive Suite 210,<br>Cedar Square Franklin, TN 37064</div>
      </div>
    </div>
    <div class="copy">
      <span>Copyright 2021 Keepwinning Personal Injury Law. All Rights Reserved.</span>
      <span><span class="soc"></span><span class="soc red"></span><span class="soc"></span><span class="soc"></span></span>
    </div>
  </div>
</footer>

</body>
</html>
```